Business cards, envelopes, etc. for real estate company

We have a finished logo for our real estate company. We need a corporate identity package with the following items:

1. Business Cards
2. Letterhead/Stationary - with 2 pages:
-1st page with full header
-2nd page without top header
3. Concise and professional e-mail signature image
4. Fax coversheet
5. Shipping label, with our return address and a mail-to address (on one label)

We need these to be editable. We don't know the industry standard for these items but perhaps you can provide them to us in .PDF and Word format (and if you use Adobe Illustrator for them, .AI as well).

Please use the attached placeholder logo in your design entry. We will provide you with the original logo to swap in (same size and design, just different text) when we choose your entry.

Please include the following information on the letterhead and business cards:

58 Birchwell Road
Suite 2B West
New York, NY 10587

Tel: 555-014-2837
Fax :555-014-2837

Please contact us if you have any questions about this contest.

Hi,

Thanks for your interest in this project. The logo to use should be working now. Please contact me if you have any further issues or questions.

I look forward to seeing your submissions. 

Hi,

We first wish to thank you all for your submissions. 

Here is some general feedback regarding the designs shown:

1. We would prefer square (as opposed to rounded) business cards.

2. For the fax coversheets, we are looking with a designed look. While we understand these are samples, we don't want it to appear as if it a standard block of text or a fax template from a word processing program.

3. For the 1st page of letterhead and envelopes, we do need an office address on them. The envelopes should have space for a stamp in the top right corner. We would prefer the envelopes not to have colored stripes.

4. We think a watermark of the logo is an interesting idea on the business cards and/or letterhead. This may be something to try. However, it is not strictly necessary and we would like to evaluate designs with and without it.

In general we are looking for a clean yet professional look.

We are actively reviewing all entries and thank you for your time and creativity.

One last comment: We understand making all objects in the brief takes some time. However, we want to remind all the designers that this contest is for more than just business cards (envelopes, letterheads, etc.) so if we choose your design, those items will be expected. Please refer to the original brief to see what we are requesting.

If you provide a mockup of any item listed in the brief (in addition to business cards) it would help us visualize your entire vision for this project.

```html
<!DOCTYPE html>
<html lang="en">
<head>
<meta charset="utf-8">
<title>Harrow &amp; Vale — Business Card</title>
<link href="https://fonts.googleapis.com/css2?family=Arimo:wght@400;700&display=swap" rel="stylesheet">
<style>
  :root {
    --page-bg: #ececec;
    --card-white: #f4f4f4;
    --card-black: #060606;
    --navy: #1f3a5a;
    --navy-dark: #1b2a48;
    --ink: #2b2b2b;
    --rule: #2a3550;
  }
  * { margin: 0; padding: 0; box-sizing: border-box; }
  html, body { width: 1200px; height: 800px; overflow: hidden; }
  body {
    background: var(--page-bg);
    font-family: "Arimo", Arial, sans-serif;
    color: var(--ink);
    position: relative;
  }
  .card {
    position: absolute;
    top: 252px;
    width: 520px;
    height: 297px;
    box-shadow: 0 6px 18px rgba(0,0,0,0.12);
  }
  .card-front { left: 50px; background: var(--card-white); }
  .card-back { left: 630px; background: var(--card-black); }

  .brand {
    position: absolute;
    left: 34px;
    top: 34px;
    display: flex;
    align-items: center;
    gap: 14px;
  }
  .brand-square { width: 46px; height: 46px; background: var(--navy); }
  .brand-name {
    font-size: 25px;
    line-height: 1.05;
    font-weight: 400;
    color: var(--navy);
  }

  .contact {
    position: absolute;
    right: 30px;
    top: 34px;
    list-style: none;
    font-size: 11px;
    line-height: 1.45;
    text-align: right;
  }
  .contact li { display: flex; justify-content: flex-end; align-items: center; gap: 7px; }
  .contact-icon { width: 11px; height: 11px; background: var(--navy-dark); display: inline-flex; }
  .contact-icon svg { width: 11px; height: 11px; }

  .divider {
    position: absolute;
    left: 34px;
    right: 30px;
    top: 122px;
    height: 1px;
    background: var(--rule);
  }

  .person { position: absolute; left: 34px; top: 150px; }
  .person-marker {
    position: absolute;
    left: -34px;
    top: 4px;
    width: 4px;
    height: 14px;
    background: var(--navy-dark);
  }
  .person-name { font-size: 17px; font-weight: 700; color: #333; }
  .person-role { font-size: 10px; font-weight: 700; color: var(--navy-dark); margin-top: 1px; }
  .address { margin-top: 18px; font-size: 11.5px; line-height: 1.35; font-style: normal; padding-left: 30px; }

  .back-brand {
    position: absolute;
    inset: 0;
    display: flex;
    align-items: center;
    justify-content: center;
    gap: 16px;
  }
  .back-brand .brand-square { width: 60px; height: 60px; background: var(--navy); }
  .back-brand .brand-name { font-size: 30px; color: #2c4e74; }
</style>
</head>
<body>
  <section class="card card-front" aria-label="Business card front">
    <div class="brand">
      <span class="brand-square"></span>
      <span class="brand-name">Harrow<br>&amp; Vale</span>
    </div>

    <ul class="contact">
      <li>555-014-2837
        <span class="contact-icon"><svg viewBox="0 0 11 11"><path d="M3 2.5l1.3 1.6-.7.9c.5 1 1.3 1.8 2.3 2.3l.9-.7 1.6 1.3-.8 1c-2.6-.4-4.7-2.5-5.1-5.1z" fill="#fff"/></svg></span>
      </li>
      <li>555-014-2837
        <span class="contact-icon"><svg viewBox="0 0 11 11"><rect x="2.5" y="4" width="6" height="4" fill="none" stroke="#fff" stroke-width=".9"/><rect x="3.5" y="2.3" width="4" height="1.7" fill="#fff"/></svg></span>
      </li>
      <li>hello@harrowvale.com
        <span class="contact-icon"><svg viewBox="0 0 11 11"><rect x="2" y="3" width="7" height="5" fill="none" stroke="#fff" stroke-width=".9"/><path d="M2 3l3.5 3L9 3" fill="none" stroke="#fff" stroke-width=".9"/></svg></span>
      </li>
      <li>www.harrowvale.com
        <span class="contact-icon"><svg viewBox="0 0 11 11"><circle cx="5.5" cy="5.5" r="3.2" fill="none" stroke="#fff" stroke-width=".9"/><path d="M2.3 5.5h6.4M5.5 2.3v6.4" stroke="#fff" stroke-width=".7"/></svg></span>
      </li>
    </ul>

    <div class="divider"></div>

    <div class="person">
      <span class="person-marker"></span>
      <p class="person-name">Daniel Reyes</p>
      <p class="person-role">Founder</p>
      <address class="address">
        58 Birchwell Road<br>
        Suite 2B West<br>
        New York, NY 10587
      </address>
    </div>
  </section>

  <section class="card card-back" aria-label="Business card back">
    <div class="back-brand">
      <span class="brand-square"></span>
      <span class="brand-name">Harrow &amp; Vale</span>
    </div>
  </section>
</body>
</html>
```